Flyer for American Indian Elders on Dementia Warning Signs

We need a flyer designed for older adults who are American Indian or Alaska Native (in the U.S.).

Ideally, the flyer should complement the colors of our logos. The project logo and our organization logo are attached to the brief.

When people see the flyer we want them to feel that it represents their culture, is warm, and professional but relatable to older adults and people who have limited incomes.

I have attached an earlier draft of the document we designed ourselves BUT we want different and better.

It is for older adults who have trouble reading so:
1. you must use a font that is 11.5 points or larger
2. Do not put text over complex pictures or use shading with words
3. You can use a serif font for the heading, but should use san serif for the body text
4. There should be good contrast between the font color and background

Please do not use any images that include a head dress or pictures of American Indian people or things that are very traditional or "token" imagery.

We need to save a small space under the call out box/ somewhere on the flyer for other people to add their logo once they download.

Let us know if you have questions or need additional information.

Target Market(s)

Older American Indian people

Font styles to use
Serif
Sans Serif

Requirements
Must have
• Easy to read for older adults
Should not have
• indian headdress

```html
<!DOCTYPE html>
<html lang="en">
<head>
<meta charset="utf-8">
<title>10 Signs of Thinking or Memory Changes That Might Be Dementia</title>
<link rel="stylesheet" href="https://fonts.googleapis.com/css2?family=Poppins:wght@600;800&family=Roboto:wght@400;700&display=swap">
<style>
  :root{
    --teal:#4fa8b3;
    --teal-dark:#3f98a2;
    --clay:#a9524e;
    --white:#ffffff;
    --ink:#222222;
    --callout-top:#6cc7cc;
    --callout-bottom:#53a9af;
  }
  *{box-sizing:border-box;margin:0;padding:0}
  html,body{width:960px;height:1200px;overflow:hidden;background:var(--white)}
  .flyer{position:relative;width:960px;height:1200px;overflow:hidden;font-family:"Roboto",Arial,sans-serif;color:var(--white)}
  .backdrop{position:absolute;inset:0;width:960px;height:1200px}

  .title{position:absolute;left:0;width:960px;text-align:center;font-family:"Poppins",Arial,sans-serif}
  .title-main{top:10px;font-weight:800;font-size:58px;line-height:60px;color:var(--teal);letter-spacing:-1.5px}
  .title-sub{top:60px;font-weight:600;font-size:33px;line-height:36px;color:var(--clay);letter-spacing:0.3px}

  .intro{position:absolute;left:53px;width:870px;font-size:17px;line-height:15.5px}
  .intro-a{top:160px}
  .intro-b{top:219px}

  .timeline{position:absolute;width:2px;background:var(--white)}
  .timeline-left{left:62px;top:285px;height:604px}
  .timeline-right{left:523px;top:287px;height:497px}

  .step-num{position:absolute;width:26px;height:26px;margin:-13px 0 0 -13px;border-radius:50%;background:var(--white);color:var(--teal);font-weight:700;font-size:15px;line-height:26px;text-align:center}
  .step-num.small{font-size:12px}

  .sign{position:absolute}
  .sign-left{left:93px;width:380px}
  .sign-right{left:555px;width:360px}
  .sign-title{font-weight:700;font-size:16.5px;line-height:19.6px;text-transform:uppercase}
  .sign-list{list-style:none;margin-top:5px}
  .sign-list li{position:relative;padding-left:24px;font-size:17px;line-height:19.8px}
  .sign-list li::before{content:"";position:absolute;left:5px;top:6px;width:8px;height:8px;border-radius:50%;background:var(--white)}
  .sign-text{font-size:17px;line-height:19.8px;margin-top:7px}

  .callout{position:absolute;left:515px;top:811px;width:416px;height:260px;border-radius:4px;background:linear-gradient(180deg,var(--callout-top),var(--callout-bottom));padding:11px 12px 0 47px}
  .callout-item{position:relative;font-size:17px;line-height:19.8px;margin-bottom:6px}
  .callout-item.strong{font-weight:700}
  .tick{position:absolute;left:-36px;top:3px;width:16px;height:16px}

  .learn-more{position:absolute;left:470px;width:494px;top:1080px;text-align:center;color:var(--ink);font-size:15.5px;line-height:20px}
  .links{position:absolute;left:470px;width:494px;top:1122px;text-align:center;color:var(--clay);font-weight:700;font-size:23px;line-height:25px}

  .partner{position:absolute;left:59px;display:flex;align-items:center;gap:12px;font-weight:700;color:var(--clay)}
  .partner-mark{flex:none;border-radius:50%;background:var(--teal)}
  .partner-one{top:960px;font-size:26px;line-height:30px}
  .partner-one .partner-mark{width:44px;height:44px}
  .partner-two{top:1030px;font-size:22px;line-height:26px;color:var(--teal-dark)}
  .partner-two .partner-mark{width:76px;height:76px;background:var(--clay)}
</style>
</head>
<body>
<main class="flyer">
  <svg class="backdrop" viewBox="0 0 960 1200" aria-hidden="true">
    <defs>
      <linearGradient id="bandGradient" x1="0" y1="0" x2="1" y2="0">
        <stop offset="0" stop-color="#a85c55"/>
        <stop offset="0.4" stop-color="#a0655f"/>
        <stop offset="0.65" stop-color="#808988"/>
        <stop offset="1" stop-color="#5a9fa3"/>
      </linearGradient>
    </defs>
    <path d="M0,104 C120,128 220,142 300,144 C420,146 520,118 600,114 C750,106 880,132 960,172" fill="none" stroke="#4fa8b3" stroke-width="7"/>
    <path d="M0,111 C120,135 220,149 300,151 C420,153 520,125 600,121 C750,113 880,139 960,179 L960,905 C700,860 500,890 300,915 C200,928 100,920 0,880 Z" fill="url(#bandGradient)"/>
    <path d="M960,910 C700,866 500,896 300,921 C200,934 100,926 0,886" fill="none" stroke="#4fa8b3" stroke-width="4"/>
  </svg>

  <h1 class="title title-main">10 SIGNS OF THINKING OR</h1>
  <h2 class="title title-sub">MEMORY CHANGES THAT MIGHT BE DEMENTIA</h2>

  <p class="intro intro-a">As we get older, we may slow down a bit. This is a normal part of aging. Changes in memory or<br>thinking that make it harder to get through the day, are not a normal part of aging. These may be early<br>signs of dementia.</p>
  <p class="intro intro-b">Because American Indian and Alaska Native people have a high risk of dementia, it is important to<br>know the warning signs. Do you have any of these 10 signs? If so, talk to your doctor.</p>

  <div class="timeline timeline-left"></div>
  <div class="timeline timeline-right"></div>

  <span class="step-num" style="left:63px;top:285px">1</span>
  <span class="step-num" style="left:63px;top:419px">2</span>
  <span class="step-num" style="left:63px;top:535px">3</span>
  <span class="step-num" style="left:63px;top:588px">4</span>
  <span class="step-num" style="left:63px;top:684px">5</span>
  <span class="step-num" style="left:63px;top:795px">6</span>
  <span class="step-num" style="left:524px;top:287px">7</span>
  <span class="step-num" style="left:524px;top:401px">8</span>
  <span class="step-num" style="left:524px;top:513px">9</span>
  <span class="step-num small" style="left:524px;top:682px">10</span>

  <section class="sign sign-left" style="top:269px">
    <h3 class="sign-title">Memory loss that affects your<br>daily life. You may</h3>
    <ul class="sign-list">
      <li>Forget events or important dates</li>
      <li>Repeat yourself</li>
      <li>Rely more often on lists or sticky<br>notes to remember things</li>
    </ul>
  </section>

  <section class="sign sign-left" style="top:405px">
    <h3 class="sign-title">Trouble planning or solving<br>problems. You may have a harder<br>time:</h3>
    <ul class="sign-list">
      <li>Paying bills</li>
      <li>Cooking recipes you have used for years</li>
    </ul>
  </section>

  <section class="sign sign-left" style="top:521px">
    <h3 class="sign-title">Get confused about the time, date,<br>or where you are.</h3>
  </section>

  <section class="sign sign-left" style="top:574px">
    <h3 class="sign-title">Daily tasks are getting harder,<br>including:</h3>
    <ul class="sign-list">
      <li>Driving</li>
      <li>Making a grocery list or going shopping</li>
    </ul>
  </section>

  <section class="sign sign-left" style="top:670px">
    <h3 class="sign-title">Trouble with how your eyesight &amp;<br>thinking work together that gets<br>worse. This includes:</h3>
    <ul class="sign-list" style="margin-top:8px">
      <li>Tripping, falls, or problems with your balance</li>
      <li>Spilling or dropping things more</li>
    </ul>
  </section>

  <section class="sign sign-left" style="top:786px">
    <h3 class="sign-title">New trouble talking or writing.</h3>
    <p class="sign-text">You have a hard time finding the words you<br>want to say. For example, you may say<br>“that thing on your wrist that tells time”<br>instead of “watch.”</p>
  </section>

  <section class="sign sign-right" style="top:269px">
    <h3 class="sign-title">Lose and cannot find things.<br>For example, you:</h3>
    <ul class="sign-list">
      <li>Can’t find the coffee pot that<br>you use every day</li>
      <li>Might put your car keys in the freezer</li>
    </ul>
  </section>

  <section class="sign sign-right" style="top:386px">
    <h3 class="sign-title">Notice changes in your mood<br>or personality, such as being</h3>
    <ul class="sign-list">
      <li>Easily mad or sad in everyday situations</li>
      <li>More fearful (scared) or suspicious<br>(not trusting)</li>
    </ul>
  </section>

  <section class="sign sign-right" style="top:498px">
    <h3 class="sign-title">Act different and make poor<br>choices. This may make you<br>more likely to:</h3>
    <ul class="sign-list">
      <li>Spend money you do not have<br>or be a scam victim</li>
      <li>Stop washing up regularly or<br>pay less attention to how you look</li>
      <li>Forget to take care of your pet</li>
    </ul>
  </section>

  <section class="sign sign-right" style="top:667px">
    <h3 class="sign-title">Pull away from friends and<br>family because it is harder<br>to keep up.</h3>
    <ul class="sign-list" style="margin-top:6px">
      <li>You may not want to do things you<br>used to enjoy, like sporting events,<br>church, music, or sex.</li>
    </ul>
  </section>

  <aside class="callout">
    <p class="callout-item"><svg class="tick" viewBox="0 0 16 16" aria-hidden="true"><circle cx="8" cy="8" r="8" fill="#fff"/><path d="M4.5,8.3 L7,10.7 L11.5,5.6" fill="none" stroke="#53a9af" stroke-width="2"/></svg>American Indian &amp; Alaska Native people<br>have a higher risk of dementia than<br>White people.</p>
    <p class="callout-item"><svg class="tick" viewBox="0 0 16 16" aria-hidden="true"><circle cx="8" cy="8" r="8" fill="#fff"/><path d="M4.5,8.3 L7,10.7 L11.5,5.6" fill="none" stroke="#53a9af" stroke-width="2"/></svg>Big changes in memory or thinking that<br>make it hard to get through the day are<br>not a normal part of aging.</p>
    <p class="callout-item"><svg class="tick" viewBox="0 0 16 16" aria-hidden="true"><circle cx="8" cy="8" r="8" fill="#fff"/><path d="M4.5,8.3 L7,10.7 L11.5,5.6" fill="none" stroke="#53a9af" stroke-width="2"/></svg>People with one or more of these 10 signs<br>should talk to their doctor to find the cause.<br>It is not always dementia.</p>
    <p class="callout-item strong"><svg class="tick" viewBox="0 0 16 16" aria-hidden="true"><circle cx="8" cy="8" r="8" fill="#fff"/><path d="M4.5,8.3 L7,10.7 L11.5,5.6" fill="none" stroke="#53a9af" stroke-width="2"/></svg>Early dementia diagnosis gives you a<br>chance to get care &amp; plan your future.</p>
  </aside>

  <p class="learn-more">To learn more about the warning signs of dementia in<br>American Indian and Alaska Native people, visit:</p>
  <p class="links">www.NativeMindWellness.org<br>www.healthyaginghub.org</p>

  <div class="partner partner-one"><span class="partner-mark"></span><span>Circle of Elders Alliance</span></div>
  <div class="partner partner-two"><span class="partner-mark"></span><span>Healthy Minds Native<br>Resource Center</span></div>
</main>
</body>
</html>
```